M Zyvantics Buisness Cards

I need a technology focused clean business card for my employees. I have attached out logo to include in the mocks. We're a modern tech consulting firm that drives to interface humanity with technology in a truly cohesive fashion.

```html
<!DOCTYPE html>
<html lang="en">
<head>
<meta charset="utf-8">
<title>M Zyvantics Business Card</title>
<link rel="stylesheet" href="https://fonts.googleapis.com/css2?family=Arimo:wght@400;700&display=swap">
<style>
  :root {
    --page-bg: #e9e7e4;
    --card-blue: #1d76bb;
    --card-grey: #808185;
    --badge-light: #f4f4f4;
    --badge-shade: #e2e2e2;
    --brand-grey: #7a7b7f;
    --brand-blue: #1d76bb;
    --text-light: #ffffff;
  }
  * { margin: 0; padding: 0; box-sizing: border-box; }
  html, body {
    width: 1200px;
    height: 900px;
    overflow: hidden;
    background: var(--page-bg);
    font-family: "Arimo", Arial, sans-serif;
  }
  .business-card {
    position: absolute;
    left: 180px;
    top: 191px;
    width: 840px;
    height: 518px;
    background: var(--card-grey);
    overflow: hidden;
    box-shadow: 0 8px 24px rgba(0,0,0,0.18);
  }
  .card-blue-panel {
    position: absolute;
    left: 0; top: 0;
    width: 564px;
    height: 100%;
    background: var(--card-blue);
  }
  .brand-badge {
    position: absolute;
    left: 348px;
    top: 34px;
    width: 450px;
    height: 450px;
    border-radius: 50%;
    background: radial-gradient(circle at 40% 35%, var(--badge-light) 0%, var(--badge-light) 55%, var(--badge-shade) 100%);
    display: flex;
    align-items: center;
    justify-content: center;
    gap: 14px;
  }
  .brand-dot {
    width: 30px;
    height: 30px;
    border-radius: 50%;
    background: var(--brand-blue);
  }
  .brand-name {
    font-weight: 700;
    font-size: 44px;
    color: var(--brand-grey);
    letter-spacing: 1px;
  }
  .holder {
    position: absolute;
    left: 49px;
    top: 60px;
    color: var(--text-light);
  }
  .holder-name {
    font-weight: 700;
    font-size: 28px;
    letter-spacing: 0.5px;
  }
  .holder-title {
    font-size: 23px;
    margin-top: 4px;
    padding-left: 2px;
  }
  .contact-list {
    position: absolute;
    left: 50px;
    top: 255px;
    list-style: none;
    color: var(--text-light);
    font-size: 23px;
  }
  .contact-list li {
    display: flex;
    align-items: center;
    height: 30px;
  }
  .contact-icon {
    width: 16px;
    height: 16px;
    margin-right: 12px;
    fill: var(--text-light);
    flex: none;
  }
  .address {
    position: absolute;
    left: 47px;
    top: 400px;
    color: var(--text-light);
    font-size: 23px;
    line-height: 31px;
    font-style: normal;
  }
</style>
</head>
<body>
  <div class="business-card">
    <div class="card-blue-panel"></div>

    <div class="holder">
      <div class="holder-name">DANIEL MERCER</div>
      <div class="holder-title">Managing Director</div>
    </div>

    <ul class="contact-list">
      <li>
        <svg class="contact-icon" viewBox="0 0 16 16" aria-hidden="true"><path d="M4 0h8a1.5 1.5 0 0 1 1.5 1.5v13A1.5 1.5 0 0 1 12 16H4a1.5 1.5 0 0 1-1.5-1.5v-13A1.5 1.5 0 0 1 4 0zm0.5 2v10.5h7V2zM8 13.3a0.9 0.9 0 1 0 0 1.8 0.9 0.9 0 0 0 0-1.8z"/></svg>
        044-555 210 384
      </li>
      <li>
        <svg class="contact-icon" viewBox="0 0 16 16" aria-hidden="true"><path d="M1 5c0-2 3-3 7-3s7 1 7 3v1.5h-3.5V5h-7v1.5H1zM4 7h8l2.5 5v2h-13v-2zM8 8.5a2 2 0 1 0 0 4 2 2 0 0 0 0-4z"/></svg>
        044-555 210 384
      </li>
      <li>
        <svg class="contact-icon" viewBox="0 0 16 16" aria-hidden="true"><path d="M0.5 3h15v10h-15zM1.8 4.2 8 9l6.2-4.8z"/></svg>
        hello@mzyvantics.com
      </li>
      <li>
        <svg class="contact-icon" viewBox="0 0 16 16" aria-hidden="true"><circle cx="8" cy="8" r="7.5"/><path d="M5 3.5c1.5 0.5 2 2 1 3s0.5 2 1.5 2.5-0.5 3 0.5 4.5M11 3c-1 1 0 2.5 1.5 2.5s2 1.5 1.5 3" stroke="#1d76bb" stroke-width="1.4" fill="none"/></svg>
        www.mzyvantics.com
      </li>
    </ul>

    <address class="address">
      48 Harbor Lane, Suite 12<br>
      Northvale, 204518.
    </address>

    <div class="brand-badge">
      <span class="brand-dot"></span>
      <span class="brand-name">M Zyvantics</span>
    </div>
  </div>
</body>
</html>
```